Verostel business card

Business card for sustainable investment company called "Verostel". Verostel is an exchange platform selling carbon credits between buyers and sellers. Carbon Credits are an environmental commodity for reducing global carbon emissions.

the card should obviously have our logo and the theme should be sustainability/environment mixed with a trading platform.

Contact Information for Business Card

Logo, Name, Title, Phone, Email

Colors
0054AA
0677BA
7BADD7
CADEEF
E8F1F8
0094D4
00A9DD
6FCCEA
C7EBF8
E9F6FB
00AB8E
00BBA5
67D7C9
C6EFE9
E9F9F6
59FF00
82FF00
B8FF75
E3FFCB
F4FFEA

```html
<!DOCTYPE html>
<html lang="en">
<head>
<meta charset="utf-8">
<title>Verostel business card</title>
<link href="https://fonts.googleapis.com/css2?family=Montserrat:wght@400;700&family=Questrial&display=swap" rel="stylesheet">
<style>
  :root {
    --backdrop: #2e2f31;
    --card: #ffffff;
    --card-shade: #ececec;
    --navy: #14305a;
    --ink: #1b2a45;
    --accent: #3a9fd6;
    --accent-light: #6fcdea;
  }
  * { margin: 0; padding: 0; box-sizing: border-box; }
  html, body {
    width: 1200px;
    height: 900px;
    overflow: hidden;
    background: var(--backdrop);
  }
  .canvas {
    position: relative;
    width: 1200px;
    height: 900px;
  }
  .card {
    position: absolute;
    left: 300px;
    width: 600px;
    height: 343px;
    background: linear-gradient(110deg, var(--card-shade) 0%, var(--card) 55%, var(--card) 100%);
    overflow: hidden;
  }
  .card--front { top: 84px; }
  .card--back { top: 473px; }

  .brand {
    position: absolute;
    display: flex;
    align-items: center;
    gap: 16px;
    left: 50%;
    transform: translateX(-50%);
  }
  .brand__square {
    width: 46px;
    height: 46px;
    background: var(--accent);
  }
  .brand__name {
    font-family: "Montserrat", sans-serif;
    font-weight: 700;
    font-size: 44px;
    letter-spacing: 1px;
    color: var(--ink);
    text-transform: uppercase;
  }
  .card--front .brand { top: 180px; }
  .card--back .brand { top: 70px; }

  .person {
    position: absolute;
    top: 166px;
    left: 0;
    width: 100%;
    text-align: center;
    color: var(--ink);
    white-space: nowrap;
  }
  .person__name {
    font-family: "Montserrat", sans-serif;
    font-weight: 700;
    font-size: 17px;
    text-transform: uppercase;
  }
  .person__divider {
    font-family: "Questrial", sans-serif;
    font-size: 19px;
    margin: 0 6px 0 10px;
  }
  .person__title {
    font-family: "Questrial", sans-serif;
    font-size: 18px;
  }

  .contact-band {
    position: absolute;
    left: 0;
    top: 226px;
    width: 100%;
    height: 58px;
    background: var(--navy);
    border-top: 2px solid var(--accent);
    border-bottom: 3px solid var(--accent-light);
    display: flex;
    align-items: center;
    justify-content: center;
    gap: 12px;
    color: #ffffff;
    font-family: "Questrial", sans-serif;
    font-size: 19px;
  }
  .contact-band__item {
    display: flex;
    align-items: center;
    gap: 8px;
  }
  .contact-band__icon { width: 18px; height: 18px; }
</style>
</head>
<body>
<main class="canvas">
  <section class="card card--front">
    <div class="brand">
      <span class="brand__square"></span>
      <span class="brand__name">Verostel</span>
    </div>
  </section>

  <section class="card card--back">
    <div class="brand">
      <span class="brand__square"></span>
      <span class="brand__name">Verostel</span>
    </div>

    <p class="person">
      <span class="person__name">Daniel Harlow</span><span class="person__divider">|</span><span class="person__title">Director</span>
    </p>

    <div class="contact-band">
      <span class="contact-band__item">
        <svg class="contact-band__icon" viewBox="0 0 24 24" aria-hidden="true">
          <path fill="#3a9fd6" d="M6.6 10.8a15.1 15.1 0 0 0 6.6 6.6l2.2-2.2c.3-.3.7-.4 1-.2 1.1.4 2.3.6 3.6.6.6 0 1 .4 1 1V20c0 .6-.4 1-1 1A17 17 0 0 1 3 4c0-.6.4-1 1-1h3.5c.6 0 1 .4 1 1 0 1.3.2 2.5.6 3.6.1.3 0 .7-.2 1l-2.3 2.2z"/>
        </svg>
        300-555-0148
      </span>
      <span>|</span>
      <span class="contact-band__item">
        <svg class="contact-band__icon" viewBox="0 0 24 24" aria-hidden="true">
          <rect x="2" y="5" width="20" height="14" rx="1.5" fill="#3a9fd6"/>
          <path d="M3 6.5l9 6.5 9-6.5" fill="none" stroke="#14305a" stroke-width="1.8"/>
        </svg>
        info@verostel.com
      </span>
    </div>
  </section>
</main>
</body>
</html>
```